Business Card

We need some ideas for corporate business cards. I'm interested in a double sided card, with one side featuring our corporate logo, the other side with employee information.

Corporate colors, logo etc. available at www.brivalo.com

Industry/Entity Type

Business

Requirements
Must have
• The "Brivalo" logo with stylized "O"

Nice to have
• Preferred font is calibri

```html
<!DOCTYPE html>
<html lang="en">
<head>
<meta charset="utf-8">
<title>Brivalo Business Card</title>
<link href="https://fonts.googleapis.com/css2?family=Caladea:wght@400;700&family=Open+Sans:wght@400;600&display=swap" rel="stylesheet">
<style>
  :root {
    --brand-blue: #4a6494;
    --paper: #ffffff;
    --ink: #1a1a1a;
    --stage: #ffffff;
    --card-shadow: 0 12px 32px rgba(0, 0, 0, 0.45);
  }
  * { margin: 0; padding: 0; box-sizing: border-box; }
  html, body {
    width: 1200px; height: 1000px; overflow: hidden;
    background: var(--stage);
  }
  .canvas { position: relative; width: 1200px; height: 1000px; }

  /* Front side */
  .card-front {
    position: absolute; left: 69px; top: 319px;
    width: 494px; height: 283px;
    background: var(--brand-blue);
    box-shadow: var(--card-shadow);
  }
  .front-wordmark {
    position: absolute; left: 0; right: 0; top: 118px;
    text-align: center;
    font-family: "Open Sans", sans-serif; font-weight: 600;
    font-size: 72px; line-height: 1; letter-spacing: 6px;
    color: var(--paper);
  }
  .front-url {
    position: absolute; left: 0; right: 0; bottom: 6px;
    text-align: center;
    font-family: "Open Sans", sans-serif; font-weight: 400;
    font-size: 17px; letter-spacing: 1.5px;
    color: var(--paper);
  }

  /* Back side */
  .card-back {
    position: absolute; left: 721px; top: 204px;
    width: 280px; height: 491px;
    background: var(--paper);
    box-shadow: var(--card-shadow);
    font-family: "Caladea", serif;
    color: var(--ink);
    text-align: center;
  }
  .back-header {
    position: absolute; left: 0; top: 21px;
    width: 278px; height: 56px;
    background: var(--brand-blue);
    display: flex; align-items: center; justify-content: center;
  }
  .back-wordmark {
    font-family: "Caladea", serif; font-weight: 700;
    font-size: 38px; letter-spacing: 4px; line-height: 1;
    color: var(--paper);
  }
  .employee {
    position: absolute; left: 0; right: 0; top: 100px;
  }
  .employee-name {
    font-weight: 700; font-size: 25px; line-height: 32px;
    color: var(--brand-blue); letter-spacing: 0.3px;
  }
  .employee-role, .employee-email {
    font-size: 20px; line-height: 26px;
  }
  .values-band {
    position: absolute; left: 0; top: 206px;
    width: 278px; height: 109px;
    background: var(--brand-blue);
  }
  .value {
    position: absolute; top: 12px;
    display: flex; flex-direction: column; align-items: center;
    color: var(--paper);
  }
  .value svg { display: block; }
  .value-label {
    position: absolute; top: 80px; white-space: nowrap;
    font-weight: 700; font-size: 15px;
  }
  .value-technology { left: 18px; }
  .value-vision { left: 97px; }
  .value-solutions { left: 207px; }
  .contact {
    position: absolute; left: 0; right: 0; top: 342px;
    font-size: 16.5px; line-height: 21px;
  }
</style>
</head>
<body>
<div class="canvas">

  <section class="card-front" aria-label="Card front">
    <div class="front-wordmark">BRIVALO</div>
    <div class="front-url">www.brivalo.com</div>
  </section>

  <section class="card-back" aria-label="Card back">
    <header class="back-header">
      <div class="back-wordmark">BRIVALO</div>
    </header>

    <div class="employee">
      <div class="employee-name">DARA M. KEANE</div>
      <div class="employee-role">Marketing Manager</div>
      <div class="employee-email">darakeane@brivalo.com</div>
    </div>

    <div class="values-band">
      <div class="value value-technology">
        <svg width="62" width="62" height="62" viewBox="0 0 62 62" aria-hidden="true">
          <g fill="var(--paper)">
            <rect x="25" y="2" width="12" height="12"/>
            <rect x="25" y="48" width="12" height="12"/>
            <rect x="2" y="25" width="12" height="12"/>
            <rect x="48" y="25" width="12" height="12"/>
            <g transform="rotate(45 31 31)">
              <rect x="25" y="2" width="12" height="12"/>
              <rect x="25" y="48" width="12" height="12"/>
              <rect x="2" y="25" width="12" height="12"/>
              <rect x="48" y="25" width="12" height="12"/>
            </g>
            <circle cx="31" cy="31" r="21"/>
          </g>
          <circle cx="31" cy="31" r="10" fill="var(--brand-blue)"/>
        </svg>
        <span class="value-label" style="left:-2px">Technology</span>
      </div>

      <div class="value value-vision">
        <svg width="90" height="62" viewBox="0 0 90 62" aria-hidden="true">
          <path d="M2 31 Q45 -8 88 31 Q45 70 2 31 Z" fill="var(--paper)"/>
          <circle cx="45" cy="31" r="17" fill="var(--brand-blue)"/>
          <circle cx="45" cy="31" r="9" fill="var(--paper)"/>
          <circle cx="45" cy="31" r="5" fill="var(--brand-blue)"/>
        </svg>
        <span class="value-label" style="left:26px">Vision</span>
      </div>

      <div class="value value-solutions">
        <svg width="62" height="62" viewBox="0 0 62 62" aria-hidden="true">
          <circle cx="31" cy="31" r="27" fill="var(--paper)"/>
          <circle cx="31" cy="31" r="20" fill="var(--brand-blue)"/>
          <path d="M41 21 L34 36 L21 41 L28 26 Z" fill="var(--paper)"/>
          <path d="M41 21 L21 41" stroke="var(--brand-blue)" stroke-width="2"/>
        </svg>
        <span class="value-label" style="left:-9px">Solutions</span>
      </div>
    </div>

    <address class="contact" style="font-style:normal">
      <div>Tel | 353 1 555 0142</div>
      <div>Fax | 353 1 555 0148</div>
      <div>14 Larkfield Road,</div>
      <div>Ashgrove Business Park</div>
      <div>Dublin, Ireland</div>
      <div>info@brivalo.com</div>
    </address>
  </section>

</div>
</body>
</html>
```